Website refresh for HollowbrookByteworks.com

I need a new fresh website with all of the information contained in hollowbrookbyteworks.com. The website needs to be built on the wix platform as it handles my booking, calendar and email marketing. The imperative pages are Home, About, Services, Clients and Testimonials. The other pages I can recreate based on the design chosen.

Industry/Entity Type

IT Services

Coding

Coded - Design and coding required

Number of Pages Required

5+ page

Font styles to use
Serif

Colors
00AB8E
00BBA5
67D7C9
C6EFE9
E9F9F6

Requirements
Must have
• I will need to be able to edit the document using the Wix WYSIWYG platform.
Nice to have
• See plovrenta.com for a look and feel.
Should not have
• n/a

```html
<!DOCTYPE html>
<html lang="en">
<head>
<meta charset="utf-8">
<title>Hollowbrook Byteworks</title>
<link href="https://fonts.googleapis.com/css2?family=Poppins:wght@400;500;600;700;800&family=Roboto+Condensed:wght@400;500;700&display=swap" rel="stylesheet">
<style>
:root{
  --teal:#00BBA5;
  --teal-dark:#00AB8E;
  --teal-mid:#67D7C9;
  --teal-pale:#C6EFE9;
  --teal-mist:#E9F9F6;
  --ink:#1a1a1a;
  --text:#333;
  --grey-bg:#f2f2f2;
  --card-bg:#f3f3f3;
  --footer:#0b0b0b;
  --star:#f7931e;
}
*{box-sizing:border-box;margin:0;padding:0}
html,body{width:1200px;height:3277px;overflow:hidden}
body{font-family:'Poppins',sans-serif;color:var(--text);background:#fff;position:relative}
.section{position:absolute;left:0;width:1200px}
.container{position:absolute;left:144px;width:912px}

/* header */
.site-header{top:0;height:83px;background:#fff}
.brand{position:absolute;left:144px;top:16px;display:flex;align-items:center;gap:10px}
.brand-mark{width:46px;height:46px;background:var(--teal-dark);border-radius:4px}
.brand-name{font-family:'Poppins',sans-serif;font-weight:700;font-size:17px;line-height:19px;color:#2a8a2a}
.main-nav{position:absolute;left:452px;top:29px;display:flex;gap:34px;font-size:15px;color:#444}
.main-nav .active{color:#222;border-bottom:2px solid var(--teal);padding-bottom:1px}
.btn{display:inline-flex;align-items:center;justify-content:center;background:var(--teal);color:#fff;font-weight:600;border-radius:22px;font-size:15px}
.header-cta{position:absolute;left:921px;top:18px;width:135px;height:41px}

/* hero */
.hero{top:83px;height:560px;background:#000;overflow:hidden}
.hero-photo{position:absolute;left:380px;top:0;width:820px;height:560px;background:linear-gradient(90deg,#000 0%,#3a3430 25%,#8c7b6c 55%,#d7d3cc 85%,#eceae6 100%)}
.hero-copy{position:absolute;left:144px;top:136px;width:440px;color:#fff}
.hero-eyebrow{color:var(--teal);font-size:24px}
.hero-title{font-size:37px;font-weight:700;margin-top:4px}
.hero-text{font-size:16.5px;line-height:24px;margin-top:8px}
.hero-cta{width:134px;height:40px;margin-top:16px}
.hero-arrows{position:absolute;left:144px;top:452px;display:flex;gap:8px}
.round-btn{width:40px;height:40px;border-radius:50%;background:#fff;display:flex;align-items:center;justify-content:center}

/* section titles */
.section-title{text-align:center;font-size:38px;color:var(--ink);font-weight:400}
.section-title b{font-weight:800}
.title-rule{width:70px;height:3px;background:var(--teal);margin:12px auto 0}

/* services */
.services{top:643px;height:500px}
.services .section-title{position:absolute;top:68px;width:100%}
.service-card{position:absolute;top:163px;width:285px;height:241px;background:linear-gradient(180deg,var(--teal) 0%,var(--teal-dark) 100%);border-radius:3px;color:#fff;text-align:center}
.service-icon{width:102px;height:102px;border-radius:50%;background:#fff;margin:38px auto 0;display:flex;align-items:center;justify-content:center}
.service-name{font-size:21px;line-height:24px;margin-top:18px}
.side-arrow{position:absolute;top:275px}

/* about */
.about{top:1143px;height:584px;background:var(--grey-bg)}
.about-photo{position:absolute;left:0;top:0;width:580px;height:584px;background:linear-gradient(160deg,#cfcac2 0%,#e4e2dd 45%,#b9b4aa 100%)}
.about-copy{position:absolute;left:621px;top:74px;width:435px}
.about-copy h2{font-size:38px;color:var(--ink);font-weight:400}
.about-copy h2 b{font-weight:800}
.about-copy .rule{width:70px;height:3px;background:var(--teal);margin:8px 0 18px}
.about-copy p{font-size:13.5px;line-height:24px;text-align:justify;margin-bottom:23px}
.about-cta{width:134px;height:40px}

/* clients */
.clients{top:1727px;height:401px;background:var(--teal-dark)}
.clients .section-title{position:absolute;top:78px;width:100%;color:#fff}
.clients .title-rule{background:#fff}
.client-logos{position:absolute;left:144px;top:175px;display:flex;gap:19px}
.client-logo{width:167px;height:87px;background:#fff;display:flex;align-items:center;justify-content:center;gap:7px;font-size:14px;font-weight:600;color:#444}
.client-logo i{width:10px;height:10px;background:var(--teal-dark);display:block}
.dots{position:absolute;top:294px;left:570px;display:flex;gap:8px}
.dots span{width:13px;height:13px;border-radius:50%;background:rgba(255,255,255,.6)}
.dots .on{background:#fff}

/* testimonials */
.testimonials{top:2128px;height:757px}
.testimonials .section-title{position:absolute;top:82px;width:100%}
.t-card{position:absolute;top:169px;width:288px;height:490px}
.t-card svg.card-shape{position:absolute;left:0;top:0}
.avatar{position:absolute;left:87px;top:0;width:114px;height:114px;border-radius:50%;background:linear-gradient(180deg,var(--teal-mid),var(--teal-dark));border:6px solid var(--teal)}
.quote-badge{position:absolute;left:127px;top:94px;width:34px;height:34px;border-radius:50%;background:#fff;font:700 26px/40px 'Poppins',serif;text-align:center;color:#222}
.stars{position:absolute;top:142px;width:100%;text-align:center;color:var(--star);font-size:15px;letter-spacing:2px}
.t-text{position:absolute;left:27px;top:170px;width:235px;font-size:16.5px;line-height:24px;text-align:justify;text-align-last:center;color:#333}
.t-name{position:absolute;top:375px;width:100%;text-align:center;font-size:19px;font-weight:700;color:#222}
.t-company{position:absolute;top:403px;width:100%;text-align:center;font-size:14px;color:#333}
.circle-arrow{position:absolute;top:412px;width:50px;height:50px;border-radius:50%;border:1.5px solid #222;display:flex;align-items:center;justify-content:center;background:#fff}

/* footer */
.site-footer{top:2885px;height:392px;background:radial-gradient(ellipse at 40% 40%,#1c1c1c 0%,var(--footer) 70%);color:#fff;font-family:'Roboto Condensed',sans-serif}
.f-col{position:absolute;top:80px}
.f-col h3{font-family:'Roboto Condensed',sans-serif;font-size:22px;font-weight:700;line-height:28px;text-transform:uppercase}
.newsletter{margin-top:20px;width:271px;height:42px;border:1px solid #555;display:flex;align-items:center;justify-content:space-between;padding:0 14px 0 17px;font-size:13px}
.socials{display:flex;gap:6px;margin-top:20px}
.socials span{width:28px;height:28px;border-radius:50%;background:#2a2a2a;display:block}
.socials .on{background:#fff}
.contact-item{display:flex;gap:18px;margin-top:20px}
.contact-item .ic{width:24px;padding-top:2px}
.contact-item b{font-size:16px;display:block}
.contact-item small{font-size:13px;display:block;margin-top:6px}
.quick-links{display:grid;grid-template-columns:136px 150px;row-gap:13px;margin-top:20px;font-size:16px}
.quick-links span::before{content:"»";color:var(--teal);margin-right:14px}
.copyright{position:absolute;top:344px;width:100%;text-align:center;font-size:15px}
</style>
</head>
<body>

<header class="section site-header">
  <div class="brand">
    <span class="brand-mark"></span>
    <span class="brand-name">Hollowbrook<br>Byteworks</span>
  </div>
  <nav class="main-nav">
    <span class="active">Home</span><span>About</span><span>Services</span><span>Clients</span><span>Testimonials</span>
  </nav>
  <a class="btn header-cta">Get Started</a>
</header>

<section class="section hero">
  <div class="hero-photo" role="img" aria-label="Smiling professional at a laptop in a bright office"></div>
  <div class="hero-copy">
    <div class="hero-eyebrow">Welcome to</div>
    <h1 class="hero-title">Hollowbrook Byteworks</h1>
    <p class="hero-text">Hollowbrook Byteworks is a Managed Service Provider for numerous small business in the Raleigh/Durham Triangle area.</p>
    <a class="btn hero-cta">Get Started</a>
  </div>
  <div class="hero-arrows">
    <span class="round-btn"><svg width="14" height="14" viewBox="0 0 14 14"><path d="M9 2 4 7l5 5" fill="none" stroke="#222" stroke-width="2"/></svg></span>
    <span class="round-btn"><svg width="14" height="14" viewBox="0 0 14 14"><path d="M5 2l5 5-5 5" fill="none" stroke="#222" stroke-width="2"/></svg></span>
  </div>
</section>

<section class="section services">
  <h2 class="section-title"><b>What</b> We Do<div class="title-rule"></div></h2>
  <svg class="side-arrow" style="left:62px" width="14" height="20" viewBox="0 0 14 20"><path d="M11 2 3 10l8 8" fill="none" stroke="#222" stroke-width="2"/></svg>
  <svg class="side-arrow" style="left:1120px" width="14" height="20" viewBox="0 0 14 20"><path d="M3 2l8 8-8 8" fill="none" stroke="#222" stroke-width="2"/></svg>
  <div class="service-card" style="left:144px">
    <div class="service-icon"><svg width="52" height="52" viewBox="0 0 52 52" fill="none" stroke="var(--teal-dark)" stroke-width="2"><rect x="8" y="12" width="36" height="26" rx="2"/><circle cx="26" cy="25" r="6"/><path d="M18 44h16M26 38v6"/></svg></div>
    <div class="service-name">Remote Maintenance<br>&amp; Monitoring</div>
  </div>
  <div class="service-card" style="left:458px">
    <div class="service-icon"><svg width="56" height="56" viewBox="0 0 56 56" fill="none" stroke="var(--teal-dark)" stroke-width="2"><circle cx="28" cy="28" r="20"/><path d="M8 28h40M28 8c-8 8-8 32 0 40M28 8c8 8 8 32 0 40"/></svg></div>
    <div class="service-name">Networking</div>
  </div>
  <div class="service-card" style="left:771px">
    <div class="service-icon"><svg width="52" height="52" viewBox="0 0 52 52" fill="none" stroke="var(--teal-dark)" stroke-width="2"><rect x="8" y="10" width="36" height="26" rx="2"/><path d="M18 42h16M26 36v6M18 28l8-10 6 6"/></svg></div>
    <div class="service-name">PC support &amp;<br>Installation</div>
  </div>
</section>

<section class="section about">
  <div class="about-photo" role="img" aria-label="Open-plan office with people working at desks"></div>
  <div class="about-copy">
    <h2><b>About</b> Us</h2>
    <div class="rule"></div>
    <p>Hollowbrook Byteworks is a Managed Service Provider for numerous small business in the Raleigh/Durham Triangle area. Our Remote Managed Services include Server Monitoring and Care, Desktop Monitoring and Care as well as Security Assessments, Optimization and Monitoring.</p>
    <p>We also provide on-site computer (both PC and Mac) repair and IT Support to small business and residential customers. We specialize in on-site computer repair.Whether your computer is infected with a Virus, Spyware, Malware, or you are looking for help managing your small business IT systems, Hollowbrook Byteworks is ready to help you in the Raleigh/Durham Triangle area.</p>
    <a class="btn about-cta">Learn More</a>
  </div>
</section>

<section class="section clients">
  <h2 class="section-title"><b>Our</b> Clients<div class="title-rule"></div></h2>
  <div class="client-logos">
    <div class="client-logo"><i></i>Ridgeline Wealth</div>
    <div class="client-logo">Calder Law Office</div>
    <div class="client-logo">Norwick Realty Law</div>
    <div class="client-logo"><i></i>Brightforge LLC</div>
    <div class="client-logo">Mapleton Law Group</div>
  </div>
  <div class="dots"><span></span><span class="on"></span><span></span></div>
</section>

<section class="section testimonials">
  <h2 class="section-title"><b>What Our</b> Clients Say<div class="title-rule"></div></h2>
  <span class="circle-arrow" style="left:47px"><svg width="14" height="14" viewBox="0 0 14 14"><path d="M9 2 4 7l5 5" fill="none" stroke="#222" stroke-width="2"/></svg></span>
  <span class="circle-arrow" style="left:1103px"><svg width="14" height="14" viewBox="0 0 14 14"><path d="M5 2l5 5-5 5" fill="none" stroke="#222" stroke-width="2"/></svg></span>

  <div class="t-card" style="left:144px">
    <svg class="card-shape" width="288" height="490" viewBox="0 0 288 490"><polygon points="0,90 288,33 288,432 0,490" fill="var(--card-bg)"/><polygon points="128,470 288,430 288,446 128,486" fill="var(--teal)"/></svg>
    <div class="avatar" role="img" aria-label="Client portrait"></div>
    <div class="quote-badge">“</div>
    <div class="stars">★★★★★</div>
    <p class="t-text">Total, complete confidence and trust - I have used their services for a number of years, for all of my equipment. They are responsive, timely and clearly state any problems with</p>
    <div class="t-name">Marla K</div>
    <div class="t-company">Company name</div>
  </div>
  <div class="t-card" style="left:456px">
    <svg class="card-shape" width="288" height="490" viewBox="0 0 288 490"><polygon points="0,90 288,33 288,432 0,490" fill="var(--card-bg)"/><polygon points="128,470 288,430 288,446 128,486" fill="var(--teal)"/></svg>
    <div class="avatar" role="img" aria-label="Client portrait"></div>
    <div class="quote-badge">“</div>
    <div class="stars">★★★★★</div>
    <p class="t-text">This letter is written in response to excellent service our firm received from Corbin Ashdale. Corbin is the principal at Hollowbrook Byteworks located in Raleigh, NC.</p>
    <div class="t-name">Dennis P</div>
    <div class="t-company">Company name</div>
  </div>
  <div class="t-card" style="left:768px">
    <svg class="card-shape" width="288" height="490" viewBox="0 0 288 490"><polygon points="0,90 288,33 288,432 0,490" fill="var(--card-bg)"/><polygon points="128,470 288,430 288,446 128,486" fill="var(--teal)"/></svg>
    <div class="avatar" role="img" aria-label="Client portrait"></div>
    <div class="quote-badge">“</div>
    <div class="stars">★★★★★</div>
    <p class="t-text">Thank you for coming by yesterday. You quickly accessed our issues and put a step by step plan together to resolve.</p>
    <div class="t-name">Tom R.</div>
    <div class="t-company">Company name</div>
  </div>
</section>

<footer class="section site-footer">
  <div class="f-col" style="left:143px">
    <h3>Subscribe to<br>our newsletter</h3>
    <div class="newsletter"><span>Email address</span><svg width="14" height="14" viewBox="0 0 14 14"><path d="M1 7 13 1 9 13 7 8z" fill="var(--teal)"/></svg></div>
    <div class="socials"><span></span><span class="on"></span><span></span><span></span><span></span></div>
  </div>
  <div class="f-col" style="left:503px">
    <h3>Contact info</h3>
    <div class="contact-item"><span class="ic"><svg width="14" height="18" viewBox="0 0 14 18"><path d="M7 1a6 6 0 0 0-6 6c0 4 6 10 6 10s6-6 6-10a6 6 0 0 0-6-6z" fill="var(--teal)"/><circle cx="7" cy="7" r="2" fill="#111"/></svg></span><div><b>Address</b><small>Lorem ipsum dolor sit amet</small></div></div>
    <div class="contact-item"><span class="ic"><svg width="20" height="14" viewBox="0 0 20 14"><rect width="20" height="14" rx="1" fill="var(--teal)"/><path d="M1 1l9 7 9-7" fill="none" stroke="#111" stroke-width="1.5"/></svg></span><div><b>Email</b><small>help@hollowbrookbyteworks.com</small></div></div>
    <div class="contact-item"><span class="ic"><svg width="18" height="18" viewBox="0 0 18 18"><path d="M4 1l3 4-2 2c1 2 3 4 5 5l2-2 4 3-2 3C8 16 2 10 1 4z" fill="var(--teal)"/></svg></span><div><b>Phone</b><small>833-BYTE WRK</small></div></div>
  </div>
  <div class="f-col" style="left:765px">
    <h3>Quick links</h3>
    <div class="quick-links">
      <span>Home</span><span>Terms and Condition</span>
      <span>About</span><span>Privacy policy</span>
      <span>Services</span><span>Help</span>
      <span>Contact</span><span>Support</span>
    </div>
  </div>
  <div class="copyright">© Copyrights 2024 | All Rights Reserved</div>
</footer>

</body>
</html>
```